Buchcover-Design für Fragenbuch
Ganz herzlichen Dank. Die Zusammenarbeit war völlig reibungslos und entspannt. Änderungswünsche wurden professionell umgesetzt und die kreativen Vorschläge fand ich super. Ich bin total glücklich mit dem Ergebnis.
Zielgruppe
Autorin und Workshopleiterin. Zielgruppe: Frauen ab 30
Aufgabenstellung
Ich benötige ein komplettes Buchcover, sowie 12 farbige Innenseiten. Es geht um ein Fragenbuch zum Ausfüllen mit dem Titel:
„Stärke jenes leise Herz
Das Arbeitsheft zum Eintragen für tiefere seelische Ruhe“
Das Format des Buches beträgt 17x22cm. Es ist in 12 Wochen unterteilt. Darum hätte ich gerne zwischen den einzelnen Wochen eine farbige Seite (1. Woche, 2. Woche etc.), die designmäßig mit dem Außencover korrespondiert.
Die Farben sollten eher zart oder gedeckt sein. Auf keinen Fall jedoch kitschig. Wichtig ist mir, dass keine bestimmte Person zu sehen ist. (Foto)
Das ist meine Website www.staerke-jenes-leise-herz.de

```html
<!DOCTYPE html>
<html lang="de">
<head>
<meta charset="utf-8">
<title>Stärke jenes leise Herz – Arbeitsheft</title>
<link rel="stylesheet" href="https://fonts.googleapis.com/css2?family=Tinos&family=Jost:wght@300;400&family=Arimo:wght@400;700&family=Mrs+Saint+Delafield&display=swap">
<style>
  :root {
    --backdrop: #e8e6e3;
    --paper: #ffffff;
    --sand: #d9cfc6;
    --sand-deep: #cbbcad;
    --tan: #c3ab8e;
    --tan-dark: #a98b6f;
    --gold-line: #c2a47a;
    --ink: #2a2220;
    --ink-soft: #4a3e38;
    --photo-candle: linear-gradient(160deg, #d9d6d3 0%, #b7b1ac 45%, #8a7466 75%, #c9b39a 100%);
    --photo-flowers: linear-gradient(135deg, #7a5c48 0%, #b4957e 45%, #d8c2ae 70%, #8c6c57 100%);
    --photo-interior: linear-gradient(150deg, #4a342a 0%, #7d5e4c 50%, #3c2a22 100%);
    --photo-dunes: linear-gradient(165deg, #e4e0da 0%, #c9c3ba 40%, #efebe5 65%, #bdb6ac 100%);
  }
  * { box-sizing: border-box; margin: 0; padding: 0; }
  html, body { width: 1200px; height: 960px; overflow: hidden; }
  body { background: var(--backdrop); position: relative; font-family: "Jost", sans-serif; color: var(--ink); }

  .page { position: absolute; top: 247px; width: 360px; height: 466px; overflow: hidden; box-shadow: 0 2px 10px rgba(0,0,0,.08); }
  .photo { position: absolute; }

  /* Week divider page */
  .week-page { left: 35px; background: var(--sand-deep); }
  .week-page .photo { left: 0; top: 0; width: 360px; height: 190px; background: var(--photo-candle); }
  .week-page .frame { position: absolute; left: 18px; right: 18px; top: 205px; bottom: 18px; border: 1px solid var(--gold-line); }
  .week-title { position: absolute; top: 258px; width: 100%; text-align: center; font-family: "Tinos", serif; font-size: 20px; letter-spacing: .5px; }
  .week-badge { position: absolute; left: 100px; top: 300px; width: 160px; height: 166px; background: var(--tan-dark); text-align: center; }
  .week-number { font-family: "Jost", sans-serif; font-weight: 300; font-size: 88px; line-height: 1; margin-top: 18px; }
  .week-label { font-family: "Jost", sans-serif; font-weight: 300; font-size: 28px; letter-spacing: 1px; }

  /* Content page */
  .content-page { left: 395px; background: var(--paper); }
  .content-page .photo-flowers { left: 30px; top: 28px; width: 310px; height: 180px; background: var(--photo-flowers); }
  .content-page .photo-interior { left: 168px; top: 232px; width: 172px; height: 160px; background: var(--photo-interior); }
  .intro-text { position: absolute; left: 34px; top: 240px; width: 118px; font-family: "Arimo", sans-serif; font-size: 7px; line-height: 1.55; color: var(--ink-soft); }
  .intro-text .rule { display: block; margin: 8px 0; }
  .intro-text strong { font-weight: 700; color: var(--ink); }
  .zigzag { position: absolute; left: 60px; top: 412px; }

  /* Cover */
  .cover { left: 805px; background: var(--sand); }
  .cover .photo { left: 0; top: 0; width: 360px; height: 210px; background: var(--photo-dunes); }
  .cover .frame { position: absolute; inset: 16px; border: 1px solid var(--gold-line); }
  .cover-title { position: absolute; top: 232px; width: 100%; text-align: center; font-family: "Tinos", serif; font-size: 20px; letter-spacing: .3px; text-transform: uppercase; }
  .cover-subtitle { position: absolute; top: 282px; width: 100%; text-align: center; font-weight: 300; font-size: 20px; text-transform: uppercase; letter-spacing: .5px; }
  .cover-claim { position: absolute; top: 314px; width: 100%; text-align: center; font-weight: 300; font-size: 9px; line-height: 1.3; text-transform: uppercase; }
  .cover-author { position: absolute; top: 342px; width: 100%; text-align: center; font-family: "Mrs Saint Delafield", cursive; font-size: 32px; }
  .cover-bar { position: absolute; left: 48px; right: 48px; bottom: 26px; height: 30px; background: var(--tan); display: flex; justify-content: space-around; align-items: center; font-family: "Tinos", serif; font-size: 8px; text-transform: uppercase; letter-spacing: .4px; }
</style>
</head>
<body>
  <section class="page week-page">
    <div class="photo" role="img" aria-label="Foto: brennende Kerze im Glas, gedeckte Töne"></div>
    <div class="frame"></div>
    <h2 class="week-title">TITLE HERE</h2>
    <div class="week-badge">
      <div class="week-number">4</div>
      <div class="week-label">WOCHE</div>
    </div>
  </section>

  <section class="page content-page">
    <div class="photo photo-flowers" role="img" aria-label="Foto: Rosen und Blätter in Sepiatönen"></div>
    <p class="intro-text">
      Nimm dir einen ruhigen Moment und lies die Fragen dieser Woche langsam durch. Notiere, was dir spontan in den Sinn kommt, ohne zu werten. Alles darf sein.
      <svg class="rule" width="40" height="6" viewBox="0 0 40 6"><polyline points="0,3 3,1 6,5 9,1 12,5 15,1 18,5 21,1 24,5 27,1 30,5 33,1 36,5 40,3" fill="none" stroke="#8a7a70" stroke-width=".7"/></svg>
      <strong>Atme tief und schreibe frei.</strong>
    </p>
    <div class="photo photo-interior" role="img" aria-label="Foto: dunkler Innenraum mit Wandleuchten"></div>
    <svg class="zigzag" width="280" height="8" viewBox="0 0 280 8">
      <polyline points="0,4 4,1 8,7 12,1 16,7 20,1 24,7 28,1 32,7 36,1 40,7 44,1 48,7 52,1 56,7 60,1 64,7 68,1 72,7 76,1 80,7 84,1 88,7 92,1 96,7 100,1 104,7 108,1 112,7 116,1 120,7 124,1 128,7 132,1 136,7 140,1 144,7 148,1 152,7 156,1 160,7 164,1 168,7 172,1 176,7 180,1 184,7 188,1 192,7 196,1 200,7 204,1 208,7 212,1 216,7 220,1 224,7 228,1 232,7 236,1 240,7 244,1 248,7 252,1 256,7 260,1 264,7 268,1 272,7 276,1 280,4" fill="none" stroke="#9a8c82" stroke-width=".8"/>
    </svg>
  </section>

  <section class="page cover">
    <div class="photo" role="img" aria-label="Foto: Sandwellen in hellen Tönen"></div>
    <div class="frame"></div>
    <h1 class="cover-title">Stärke jenes leise Herz</h1>
    <p class="cover-subtitle">Das Arbeitsheft</p>
    <p class="cover-claim">Zum Eintragen<br>für tiefere seelische Ruhe</p>
    <p class="cover-author">by Lene Hartwig</p>
    <div class="cover-bar"><span>Coaching</span><span>Mentoring</span><span>2021</span></div>
  </section>
</body>
</html>
```